Web Concept Design - modernize website

Looking to modernize our current website. http :// hwmcalderbrook . com

Color Scheme: Use uploaded palette. (Black, Silver, Dark Purple, Greyish Blue)

The website needs to have a patient-friendly, community-friendly feel to it. While still being a professional medical website. We don't want it to have a cold, clinical feel.

Information on home page needs to be split into their own separate pages with designs for each.

Home Page:
Harbor Walk Medical & Family Care is a family practice and urgent care clinic dedicated to providing high quality, compassionate health care, to patients of all ages.
Hours of operation:
Monday-Friday 9am-6:30pm
Saturday: CLOSED
Sunday: CLOSED
Primary Care visits will be by appointment only.
We will accept our last new patient at 6:00p and our last established patient at 6:30p.
We will no longer be doing DOT Physicals.

At bottom of home page:

Harbor Walk Medical & Family Care understands that information about your health is private and we know how important it is to keep your medical information protected. We follow all HIPAA guidelines to protect the privacy of your medical records. The privacy act below explains our privacy practices and how we may use and disclose your medical information. If you would like for Harbor Walk Medical & Family Care to release any or all of your medical information to others, you can make the request by signing a release and bring it with you at your next visit. If you would like to contact someone about the privacy and/or use of your medical information, you may contact us at 205-318-7702.

Click here for HIPAA document.

Click here for Medical Release form.

---------------

Services Page:
We provide family and urgent care for patients of all ages.

-Annual physicals
-Pre-employment drug screening
-Women's care including pap smears
-Screening and treatment for diabetes, hypertension and cholesterol
-All minor trauma such as abscesses, lacerations, burns and fractures
-Minor skin complaints
-Onsite LAB/XRAY/EKG
-Weight loss
-Adult and Pediatric Vaccinations
-Osteopathic manual medicine
-Medical pain management

-----

Payment & Insurance Page:
We now have online bill pay for patient balances. Please visit https://secure.paylumenclinic.com/hwmc382pay to pay your bill today!

We currently accept all forms of insurance with the exception of Medicaid. Please bring a copy of your insurance card and photo ID upon visit. We are also a Veltrona prime provider. We do accept self-pay for patients who do not have insurance.

----

Meet Our Providers Page:

Dr. Leonard (Len) Maddox, DO
Family Practice Physician

Professional Experience
April 4, 2010 to Present Harbor Walk Medical & Family Care Owner
12 years of Emergency Medicine experience
6/1994 - 7/1997 KSU Birmingham, AL
Family Medicine Residency
10/1997 to Present Board Certified in Family Medicine
Recertified 2004
Education
9/1990 to 5/1994 Eastbrook College of Osteopathic Medicine
Fenwick Hollow, New York
Degree: Doctor of Osteopathic Medicine
9/1985 to 5/1989 Carrowfield-Pinecrest College
Birmingham, Alabama
Degree: Bachelor of Science
Membership
National Guild of Household Clinicians
Physicians Union of the Gulf Territories

----

Navigation Bar should have links for all the above pages + NEW PATIENTS + Access Your Medical Records (feel free to be creative with how you design this). We don't want the navigation bar to be too crowded.

Target Market(s)

Medical Patients

Number of Pages Required

5+ page

Colors

Designer to choose colors to be used in the design.

Requirements
Must have
• Designs for all pages
• Keep it professional
Nice to have
• Be creative!
Should not have
• No cold clinical, medical websites

```html
<!DOCTYPE html>
<html lang="en">
<head>
<meta charset="utf-8">
<title>Harbor Walk Medical &amp; Family Care</title>
<link href="https://fonts.googleapis.com/css2?family=Lato:ital,wght@0,400;0,700;1,400;1,700&display=swap" rel="stylesheet">
<style>
:root{
  --black:#121212;
  --ink:#333333;
  --purple:#3e0e6c;
  --blue:#7da6c5;
  --blue-dark:#6f98b8;
  --silver:#e6e6e6;
  --panel:#eeeeee;
  --white:#ffffff;
  --muted:#b9b9b9;
}
*{box-sizing:border-box;margin:0;padding:0}
html,body{width:717px;height:1200px;overflow:hidden;background:var(--white)}
body{position:relative;font-family:'Lato',sans-serif;color:var(--ink)}
.abs{position:absolute}

/* header */
.site-header{left:0;top:0;width:717px;height:86px;background:var(--black)}
.brand{left:45px;top:24px;color:var(--white);font-size:15px;line-height:18px;font-weight:400}
.brand .line2{display:block;padding-left:64px}
.contact{top:18px;font-size:11.5px;font-weight:700;color:var(--blue);display:flex;align-items:center;gap:7px}
.contact.phone{left:424px}
.contact.mail{left:529px;font-size:9.5px}
.header-btn{top:50px;height:24px;background:linear-gradient(#ffffff,#e2e2e2);color:#111;font-size:8.4px;font-weight:700;display:flex;align-items:center;justify-content:center;border-radius:2px}

/* nav */
.main-nav{left:0;top:86px;width:717px;height:32px;background:var(--blue)}
.nav-link{top:0;line-height:32px;color:var(--white);font-size:9px;font-weight:700;letter-spacing:.2px}

/* hero */
.hero{left:0;top:118px;width:717px;height:279px;background:var(--silver)}
.hero-photo{left:242px;top:0;width:475px;height:279px;background:linear-gradient(100deg,#f1f1f1 0%,#dfe3e6 45%,#c9ced2 100%)}
.hero-title{left:45px;top:78px;color:var(--purple);font-size:31px;line-height:30px;font-weight:700;font-style:italic}
.hero-sub{left:46px;top:145px;font-size:15.5px;line-height:21px;color:#3a3a3a}
.dots{left:45px;top:248px;display:flex;gap:6px}
.dots span{width:7px;height:7px;border-radius:50%;background:#6b6b6b}
.dots span.active{background:var(--blue)}

/* welcome */
.welcome-title{left:0;top:436px;width:717px;text-align:center;color:var(--purple);font-size:15px;font-weight:400;letter-spacing:.3px}
.welcome-text{left:95px;top:465px;width:527px;text-align:center;font-size:11px;line-height:16px;color:#444}
.btn{background:linear-gradient(#8ab1ce,var(--blue-dark));color:var(--white);font-size:8.6px;font-weight:700;display:flex;align-items:center;justify-content:center;border-radius:1px;letter-spacing:.2px}

/* services */
.services{left:0;top:581px;width:358px;height:285px;background:var(--black);color:var(--white)}
.services-photo{left:358px;top:581px;width:359px;height:285px;background:linear-gradient(120deg,#cfd8df 0%,#8fa9c3 45%,#c9bca6 100%)}
.services-title{left:45px;top:32px;font-size:14px;letter-spacing:.4px}
.services-intro{left:45px;top:63px;font-size:9px}
.service-list{left:45px;top:79px;list-style:none}
.service-list li{display:flex;align-items:center;height:17.6px;font-size:8.8px}
.service-list svg{margin-right:12px;flex:none}

/* privacy + hours */
.privacy-text{left:45px;top:893px;width:415px;font-size:8.9px;line-height:16px;color:#444}
.hours{left:474px;top:897px;width:199px;height:182px;background:var(--panel);padding:14px 11px}
.hours h3{color:var(--purple);font-size:11.5px;font-weight:400;letter-spacing:.2px;margin-bottom:10px}
.hours-row{display:flex;font-size:8.2px;color:#222;height:19.2px}
.hours-row span:first-child{width:79px}
.hours .note{margin-top:7px;color:var(--purple);font-size:8.6px;font-weight:700;line-height:11px}
.hours .fine{margin-top:3px;font-size:7.4px;font-style:italic;line-height:12px;color:#333}

/* footer */
.site-footer{left:0;top:1106px;width:717px;height:94px;background:var(--black)}
.footer-link{top:30px;color:var(--white);font-size:8px;font-weight:700}
.copyright{left:45px;top:56px;font-size:7.8px;color:var(--muted)}
.social{left:569px;top:44px;display:flex;gap:12px}
.social span{width:12px;height:12px;border-radius:50%;background:var(--white)}
</style>
</head>
<body>

<header class="abs site-header">
  <div class="abs brand">Harbor Walk Medical &amp;<span class="line2">Family Care</span></div>
  <div class="abs contact phone">
    <svg width="9" height="9" viewBox="0 0 24 24"><path fill="#fff" d="M6.6 10.8a15 15 0 0 0 6.6 6.6l2.2-2.2c.3-.3.7-.4 1-.2 1.1.4 2.3.6 3.6.6.6 0 1 .4 1 1V20c0 .6-.4 1-1 1A17 17 0 0 1 3 4c0-.6.4-1 1-1h3.5c.6 0 1 .4 1 1 0 1.2.2 2.4.6 3.6.1.3 0 .7-.2 1z"/></svg>
    205.318.7702
  </div>
  <div class="abs contact mail">
    <svg width="10" height="8" viewBox="0 0 20 15"><rect width="20" height="15" rx="1" fill="#fff"/><path d="M1 1l9 7 9-7" stroke="#121212" stroke-width="1.6" fill="none"/></svg>
    harborwalkcare@lumenmail.com
  </div>
  <div class="abs header-btn" style="left:410px;width:97px">NEW PATIENTS</div>
  <div class="abs header-btn" style="left:512px;width:161px">ACCESS YOUR MEDICAL RECORDS</div>
</header>

<nav class="abs main-nav">
  <span class="abs nav-link" style="left:45px">HOME</span>
  <span class="abs nav-link" style="left:103px">SERVICES</span>
  <span class="abs nav-link" style="left:175px">PAYMENT &amp; INSURANCE</span>
  <span class="abs nav-link" style="left:312px">MEET OUR PROVIDERS</span>
  <span class="abs nav-link" style="left:442px">CONTACT US</span>
</nav>

<section class="abs hero">
  <div class="abs hero-photo" role="img" aria-label="Photo of a doctor writing on a clipboard beside a patient in a hospital room"></div>
  <h1 class="abs hero-title">Harbor Walk Medical &amp;<br>Family Care</h1>
  <p class="abs hero-sub">High Quality,<br>Compassionate Health Care</p>
  <div class="abs dots"><span class="active"></span><span></span><span></span><span></span></div>
</section>

<h2 class="abs welcome-title">WELCOME TO OUR WEBSITE</h2>
<p class="abs welcome-text">Harbor Walk Medical &amp; Family Care is a family practice and urgent care clinic dedicated to providing high quality, compassionate health care, to patients of all ages.</p>
<div class="abs btn" style="left:315px;top:517px;width:87px;height:25px">READ MORE</div>

<section class="abs services">
  <h2 class="abs services-title">OUR SERVICES</h2>
  <p class="abs services-intro">We provide family and urgent care for patients of all ages.</p>
  <ul class="abs service-list">
    <li><svg width="8" height="8" viewBox="0 0 16 16"><circle cx="8" cy="8" r="8" fill="#7da6c5"/><path d="M4.5 8.3l2.3 2.3 4.7-4.8" stroke="#121212" stroke-width="2" fill="none"/></svg>Annual physicals</li>
    <li><svg width="8" height="8" viewBox="0 0 16 16"><circle cx="8" cy="8" r="8" fill="#7da6c5"/><path d="M4.5 8.3l2.3 2.3 4.7-4.8" stroke="#121212" stroke-width="2" fill="none"/></svg>Pre-employment drug screening</li>
    <li><svg width="8" height="8" viewBox="0 0 16 16"><circle cx="8" cy="8" r="8" fill="#7da6c5"/><path d="M4.5 8.3l2.3 2.3 4.7-4.8" stroke="#121212" stroke-width="2" fill="none"/></svg>Women's care including pap smears</li>
    <li><svg width="8" height="8" viewBox="0 0 16 16"><circle cx="8" cy="8" r="8" fill="#7da6c5"/><path d="M4.5 8.3l2.3 2.3 4.7-4.8" stroke="#121212" stroke-width="2" fill="none"/></svg>Screening and treatment for diabetes, hypertension and cholesterol</li>
    <li><svg width="8" height="8" viewBox="0 0 16 16"><circle cx="8" cy="8" r="8" fill="#7da6c5"/><path d="M4.5 8.3l2.3 2.3 4.7-4.8" stroke="#121212" stroke-width="2" fill="none"/></svg>All minor trauma such as abscesses, lacerations, burns and fractures</li>
    <li><svg width="8" height="8" viewBox="0 0 16 16"><circle cx="8" cy="8" r="8" fill="#7da6c5"/><path d="M4.5 8.3l2.3 2.3 4.7-4.8" stroke="#121212" stroke-width="2" fill="none"/></svg>Minor skin complaints</li>
    <li><svg width="8" height="8" viewBox="0 0 16 16"><circle cx="8" cy="8" r="8" fill="#7da6c5"/><path d="M4.5 8.3l2.3 2.3 4.7-4.8" stroke="#121212" stroke-width="2" fill="none"/></svg>Onsite LAB/XRAY/EKG</li>
  </ul>
  <div class="abs btn" style="left:45px;top:222px;width:126px;height:25px">VIEW ALL SERVICES</div>
</section>
<div class="abs services-photo" role="img" aria-label="Photo of a doctor shaking hands with a smiling senior couple"></div>

<p class="abs privacy-text">Harbor Walk Medical &amp; Family Care understands that information about your health is private and we know how important it is to keep your medical information protected. We follow all HIPAA guidelines to protect the privacy of your medical records. The privacy act below explains our privacy practices and how we may use and disclose your medical information. If you would like for Harbor Walk Medical &amp; Family Care to release any or all of your medical information to others, you can make the request by signing a release and bring it with you at your next visit. If you would like to contact someone about the privacy and/or use of your medical information, you may contact us at 205-318-7702.</p>
<div class="abs btn" style="left:45px;top:1024px;width:176px;height:25px">CLICK HERE FOR HIPAA DOCUMENT</div>
<div class="abs btn" style="left:45px;top:1054px;width:201px;height:25px">CLICK HERE FOR MEDICAL RELEASE FORM</div>

<aside class="abs hours">
  <h3>HOURS OF OPERATION:</h3>
  <div class="hours-row"><span>Monday-Friday</span><span>9am-6:30pm</span></div>
  <div class="hours-row"><span>Saturday:</span><span>CLOSED</span></div>
  <div class="hours-row"><span>Sunday:</span><span>CLOSED</span></div>
  <p class="note">Primary Care visits will be by appointment only.</p>
  <p class="fine">We will accept our last new patient at 6:00p and our last established patient at 6:30p. We will no longer be doing DOT Physicals.</p>
</aside>

<footer class="abs site-footer">
  <span class="abs footer-link" style="left:45px">HOME</span>
  <span class="abs footer-link" style="left:96px">SERVICES</span>
  <span class="abs footer-link" style="left:158px">PAYMENT &amp; INSURANCE</span>
  <span class="abs footer-link" style="left:278px">MEET OUR PROVIDERS</span>
  <span class="abs footer-link" style="left:393px">CONTACT US</span>
  <p class="abs copyright">Copyright © 2018 Comapny Name. All Rights Reserved.</p>
  <div class="abs social" aria-label="Social media links"><span></span><span></span><span></span><span></span><span></span></div>
</footer>

</body>
</html>
```